Stationary & Business Card for Talvo Co, LLC
Talvo Co, LLC
Professional
Adrian Pellworth, MD
President
2918 Larkfield Ave., Suite C-240
Bethesda, MD 20846
dradrian@talvocollc.com
www.talvocollc.com
Our tagline is Your Partner in Personalized Healthcare.
We would like a solid color for our back - either matching the purple or gold of our logo

```html
<!DOCTYPE html>
<html lang="en">
<head>
<meta charset="utf-8">
<title>Talvo Co, LLC — Stationery</title>
<link href="https://fonts.googleapis.com/css2?family=Lato:wght@400;700&family=Playfair+Display:wght@500&display=swap" rel="stylesheet">
<style>
  :root{
    --purple:#4e2a6b;
    --purple-dark:#3d1f56;
    --gold:#c9a13b;
    --paper:#ffffff;
    --stage:#e9eaec;
    --ink:#5a5a5a;
    --faint:#e4e2e8;
  }
  *{box-sizing:border-box;margin:0;padding:0}
  html,body{width:1200px;height:936px;overflow:hidden}
  body{background:var(--stage);position:relative;font-family:"Lato",sans-serif;color:var(--ink)}
  .piece{position:absolute;background:var(--paper);overflow:hidden}
  .piece svg.waves{position:absolute;left:0;bottom:0;display:block}
  .brand{display:flex;align-items:center;gap:8px;color:var(--purple);font-family:"Playfair Display",serif;font-weight:500;white-space:nowrap}
  .brand .dot{border-radius:50%;background:var(--purple);flex:none}
  .tagline{font-size:7px;color:var(--gold);letter-spacing:.4px;text-transform:uppercase}
  .url{position:absolute;color:#fff;font-weight:700;letter-spacing:3px;white-space:nowrap}
  .small{font-size:6px;line-height:1.5;color:var(--ink)}

  /* Letterhead */
  .letterhead{left:86px;top:30px;width:484px;height:585px}
  .letterhead .brand{position:absolute;left:50%;top:28px;transform:translateX(-50%);font-size:22px}
  .letterhead .brand .dot{width:28px;height:28px}
  .letterhead .seal{position:absolute;left:172px;top:230px;width:140px;height:140px;border-radius:50%;background:var(--faint)}
  .letterhead .footer{position:absolute;left:28px;bottom:20px;right:28px;display:flex;justify-content:space-between;color:#fff;font-size:6.5px}

  /* Folder */
  .folder{left:633px;top:30px;width:493px;height:640px}
  .folder .brand{position:absolute;left:60px;top:190px;font-size:40px}
  .folder .brand .dot{width:62px;height:62px}
  .folder .brand .rule{width:2px;height:62px;background:var(--gold)}
  .folder .tagline{position:absolute;left:142px;top:258px}
  .folder .url{left:0;right:0;text-align:center;bottom:36px;font-size:15px}

  /* Business cards */
  .card-front{left:30px;top:721px;width:205px;height:89px}
  .card-front .brand{position:absolute;left:10px;top:8px;font-size:13px;gap:5px}
  .card-front .brand .dot{width:16px;height:16px}
  .card-front .person{position:absolute;left:10px;top:34px;font-size:6.5px;color:var(--purple);font-weight:700}
  .card-front .person span{display:block;font-weight:400;color:var(--ink);font-size:5.5px}
  .card-front .contact{position:absolute;left:10px;top:54px;font-size:5px}
  .card-back{left:30px;top:825px;width:205px;height:89px}
  .card-back .mark{position:absolute;left:14px;top:10px;width:58px;height:58px;border-radius:50%;background:var(--purple)}
  .card-back .url{right:10px;bottom:8px;font-size:7px;letter-spacing:1.5px}

  /* Envelopes */
  .envelope{left:253px;top:721px;width:395px;height:193px}
  .envelope .brand{position:absolute;left:18px;top:14px;font-size:18px;gap:6px}
  .envelope .brand .dot{width:24px;height:24px}
  .envelope .sender{position:absolute;left:18px;top:46px;font-size:5.5px}
  .envelope .url{left:0;right:0;text-align:center;bottom:16px;font-size:10px}
  .envelope-back{left:668px;top:721px;width:496px;height:190px}
  .envelope-back .site{position:absolute;left:0;right:0;top:30px;text-align:center;font-size:11px;letter-spacing:3px;color:var(--purple);font-weight:700}
</style>
</head>
<body>

<section class="piece letterhead" aria-label="Letterhead">
  <div class="brand"><span class="dot"></span>Talvo Co, LLC</div>
  <div class="seal" aria-hidden="true"></div>
  <svg class="waves" width="484" height="140" viewBox="0 0 484 140" aria-hidden="true">
    <path d="M0,58 C160,92 330,66 484,12 L484,30 C330,84 160,108 0,74Z" fill="var(--gold)"/>
    <path d="M0,74 C160,108 330,84 484,30 L484,140 L0,140Z" fill="var(--purple)"/>
  </svg>
  <div class="footer">
    <span>2918 Larkfield Ave., Suite C-240 · Bethesda, MD 20846</span>
    <span>(301) 555-0142 · dradrian@talvocollc.com</span>
  </div>
</section>

<section class="piece folder" aria-label="Presentation folder">
  <div class="brand"><span class="dot"></span><span class="rule"></span>Talvo Co, LLC</div>
  <div class="tagline">Your Partner in Personalized Healthcare</div>
  <svg class="waves" width="493" height="150" viewBox="0 0 493 150" aria-hidden="true">
    <path d="M0,40 C170,84 340,60 493,10 L493,28 C340,78 170,102 0,58Z" fill="var(--gold)"/>
    <path d="M0,58 C170,102 340,78 493,28 L493,150 L0,150Z" fill="var(--purple)"/>
  </svg>
  <div class="url">www.talvocollc.com</div>
</section>

<section class="piece card-front" aria-label="Business card front">
  <div class="brand"><span class="dot"></span>Talvo Co, LLC</div>
  <div class="person">Adrian Pellworth, MD<span>President</span></div>
  <div class="small contact">2918 Larkfield Ave., Suite C-240, Bethesda, MD 20846<br>(301) 555-0142 · dradrian@talvocollc.com</div>
  <svg class="waves" width="205" height="22" viewBox="0 0 205 22" aria-hidden="true">
    <path d="M0,14 C70,22 140,16 205,4 L205,8 C140,20 70,26 0,18Z" fill="var(--gold)"/>
    <path d="M0,18 C70,26 140,20 205,8 L205,22 L0,22Z" fill="var(--purple)"/>
  </svg>
</section>

<section class="piece card-back" aria-label="Business card back">
  <div class="mark" aria-hidden="true"></div>
  <svg class="waves" width="205" height="24" viewBox="0 0 205 24" aria-hidden="true">
    <path d="M0,12 C70,2 140,4 205,6 L205,9 C140,7 70,5 0,15Z" fill="var(--gold)"/>
    <path d="M0,15 C70,5 140,7 205,9 L205,24 L0,24Z" fill="var(--purple)"/>
  </svg>
  <div class="url">www.talvocollc.com</div>
</section>

<section class="piece envelope" aria-label="Envelope front">
  <div class="brand"><span class="dot"></span>Talvo Co, LLC</div>
  <div class="small sender">2918 Larkfield Ave., Suite C-240<br>Bethesda, MD 20846</div>
  <svg class="waves" width="395" height="70" viewBox="0 0 395 70" aria-hidden="true">
    <path d="M0,20 C130,44 270,34 395,8 L395,18 C270,44 130,54 0,30Z" fill="var(--gold)"/>
    <path d="M0,30 C130,54 270,44 395,18 L395,70 L0,70Z" fill="var(--purple)"/>
  </svg>
  <div class="url">www.talvocollc.com</div>
</section>

<section class="piece envelope-back" aria-label="Envelope back">
  <div class="site">www.talvocollc.com</div>
  <svg class="waves" width="496" height="120" viewBox="0 0 496 120" aria-hidden="true">
    <path d="M0,30 C160,66 336,66 496,30 L496,40 C336,76 160,76 0,40Z" fill="var(--gold)"/>
    <path d="M0,40 C160,76 336,76 496,40 L496,120 L0,120Z" fill="var(--purple)"/>
  </svg>
</section>

</body>
</html>
```